Natural Organic Cosmetics needs a packaging design

I need package design designs for an organic, natural, unrefined shea butter packaged in a pouch like the example below. The package design should express pure, organic, freshness, moisturizing and healthy. The package design should also reflect the benefits of the product listed below. The product will be called “ORGANIC SHEA BUTTER”
MEANING OF NAME: ZENO AFRICA" meaning to Come to Africa for your natural cosmetics
Logo Text/Brand Name:
“ZENO”
Logo Styles of Interest:
Elegance
Natural
Organic
Freshness
Unrefined
From a tree nut
Target Market:
General public
Must have:
KISS : Keep it simple stupid
Note: I have a shea nuts stock photo i can provide.
Dimension:W = 7.48 InchesH = 10.43 inches Added Thursday, January 14, 2016
Industry/Entity Type
Cosmetics

```html
<!DOCTYPE html>
<html lang="en">
<head>
<meta charset="utf-8">
<title>ZENO Shea Butter – Pouch Label</title>
<link rel="stylesheet" href="https://fonts.googleapis.com/css2?family=Kalam:wght@400;700&family=Montserrat:wght@900&family=Roboto+Condensed:wght@400;700&display=swap">
<style>
  :root {
    --brand-red: #7d0b0b;
    --text-red: #8a1d16;
    --cream: #f6e6bf;
    --panel-top: #efd9a4;
    --panel-mid: #f6e7b9;
    --panel-low: #fbefc4;
    --ink: #1d1a16;
    --rule: #c98a6a;
    --art-light: #e6d9a2;
    --art-dark: #cfc48f;
  }
  * { box-sizing: border-box; margin: 0; padding: 0; }
  html, body { width: 1200px; height: 738px; overflow: hidden; background: #ffffff; }
  .sheet { position: relative; width: 1200px; height: 738px; }

  .label {
    position: absolute; top: 40px; width: 473px; height: 658px; overflow: hidden;
    background: linear-gradient(180deg, var(--panel-top) 0%, var(--panel-mid) 45%, var(--panel-low) 100%);
  }
  .label--front { left: 120px; }
  .label--back { left: 607px; }

  .brand-band {
    position: absolute; background: var(--brand-red);
    display: flex; align-items: center; justify-content: center;
  }
  .brand-name {
    font-family: "Montserrat", sans-serif; font-weight: 900; color: var(--cream);
    letter-spacing: 1px; line-height: 1;
  }
  .label--front .brand-band { left: 0; top: 97px; width: 473px; height: 86px; }
  .label--front .brand-name { font-size: 66px; }
  .label--back .brand-band { left: 119px; top: 63px; width: 233px; height: 42px; }
  .label--back .brand-name { font-size: 33px; }

  .script { position: absolute; left: 0; width: 100%; text-align: center; font-family: "Kalam", cursive; white-space: nowrap; }
  .product-name { color: var(--ink); font-weight: 400; }
  .product-claim { color: var(--text-red); }
  .product-traits { color: var(--ink); }
  .dot { font-size: 0.55em; vertical-align: 0.2em; padding: 0 0.25em; }
  .rule {
    position: absolute; height: 1px;
    background: linear-gradient(90deg, transparent, var(--rule) 20%, var(--rule) 80%, transparent);
  }

  .label--front .product-name { top: 190px; font-size: 48px; line-height: 60px; }
  .label--front .product-claim { top: 248px; font-size: 21px; line-height: 28px; }
  .label--front .product-traits { top: 500px; font-size: 23px; line-height: 32px; }
  .label--front .rule { left: 72px; top: 539px; width: 330px; }
  .net-weight { top: 585px; font-size: 18px; line-height: 19px; color: var(--ink); }

  .leaf-ring {
    position: absolute; left: 76px; top: 276px; width: 324px; height: 300px; border-radius: 50%;
    background: radial-gradient(circle, rgba(200,190,150,0.22) 0%, rgba(200,190,150,0.14) 60%, transparent 72%);
  }
  .hero-art {
    position: absolute; left: 80px; top: 310px; width: 312px; height: 182px; border-radius: 8px;
    background: linear-gradient(180deg, var(--art-light) 0%, var(--art-dark) 100%);
  }

  .label--back .product-name { top: 104px; font-size: 25px; line-height: 28px; }
  .label--back .product-claim { top: 129px; font-size: 9.5px; line-height: 12px; }
  .label--back .product-traits { top: 148px; font-size: 17px; line-height: 24px; }
  .label--back .rule { left: 129px; top: 176px; width: 216px; }

  .info-box {
    position: absolute; border: 2px solid var(--text-red); border-radius: 16px;
    font-family: "Roboto Condensed", sans-serif; color: var(--text-red);
    font-size: 8.6px; line-height: 11.2px;
  }
  .info-box p + p { margin-top: 11px; }
  .info-box--about { left: 83px; top: 194px; width: 306px; height: 204px; padding: 14px 10px 0 12px; text-align: justify; }
  .info-box--about p:first-child { text-align: center; }
  .info-box--notice { left: 83px; top: 406px; width: 306px; height: 101px; padding: 8px 14px 0; text-align: center; }
  .info-box--storage { left: 129px; top: 516px; width: 260px; height: 40px; padding: 4px 6px 0; text-align: center; font-size: 7px; line-height: 9.4px; border-radius: 14px; }
  .storage-title { font-weight: 700; font-size: 7.6px; }
  .info-box--storage .storage-body { margin-top: 1px; }

  .credits {
    position: absolute; top: 566px; font-family: "Roboto Condensed", sans-serif;
    color: var(--text-red); font-size: 9.6px; line-height: 12px;
  }
  .credits--distributor { left: 159px; }
  .credits--producer { left: 285px; }

  .spec {
    position: absolute; top: 703px; font-family: Arial, Helvetica, sans-serif;
    font-size: 13px; color: #111111; white-space: nowrap;
  }
  .spec--front { left: 122px; }
  .spec--back { right: 120px; }
</style>
</head>
<body>
<main class="sheet">
  <section class="label label--front" aria-label="Front label">
    <div class="brand-band"><span class="brand-name">ZENO</span></div>
    <h1 class="script product-name">Shea Butter</h1>
    <p class="script product-claim">100% Natural &amp; Organic</p>
    <div class="leaf-ring" role="img" aria-label="Faint circular wreath of leaves"></div>
    <div class="hero-art" role="img" aria-label="Illustration of shea nuts in front of sunrise over farm fields"></div>
    <p class="script product-traits">Organic<span class="dot">&#9679;</span>Unrefined<span class="dot">&#9679;</span>Natural</p>
    <div class="rule"></div>
    <p class="script net-weight">16 OZ.<br>External Use Only</p>
  </section>

  <section class="label label--back" aria-label="Back label">
    <div class="brand-band"><span class="brand-name">ZENO</span></div>
    <h2 class="script product-name">Shea Butter</h2>
    <p class="script product-claim">100% Natural &amp; Organic</p>
    <p class="script product-traits">Organic<span class="dot">&#9679;</span>Unrefined<span class="dot">&#9679;</span>Natural</p>
    <div class="rule"></div>

    <div class="info-box info-box--about">
      <p>ZENO Shea Butter is 100% natural, unrefined and produced from an edible nut produced by the Shea Tree (Karite). This tree is commonly found in parts of Western and Central Africa including: Ghana, Mali, and Burkina Faso.</p>
      <p>Shea butter nourishes the skin with Vitamins A, E and F. Vitamins A and E maintain the skin and keep it clear and healthy. They are particularly helpful for sun damaged skin and to help prevent premature wrinkles and facial lines. The Vitamin A in shea butter is important for improving skin conditions, including blemishes, wrinkles, eczema, and dermatitis. Vitamin F acts as a protector and rejuvenator soothing rough dry or chapped skin and helps soften dry or damaged hair.</p>
      <p>The rich, creamy texture and high content of non-saponifible fats (Vitamin F) in the Shea Butter make it an ideal moisturizer. It can be added to skin care formulations or used by itself to assist with aging skin, eczema, dryness and relief from irritation. Shea Butter can also be used on the hair to moisturize a dry scalp and stimulate hair growth.</p>
    </div>

    <div class="info-box info-box--notice">
      <p>Shea butter benefits listed above are generally accepted by the public as the benefits of the natural butter.</p>
      <p>These statements have not been evaluated by the FDA or other authorities. This product is not intended to diagnose, treat, cure or prevent any disease.</p>
      <p>Products may vary slightly in color and appearance due to being all-natural products.</p>
    </div>

    <div class="info-box info-box--storage">
      <p class="storage-title">STORE IN A COOL DRY PLACE AND AVOID DIRECT SUNLIGHT</p>
      <p class="storage-body">Vegetable butters may melt or partially melt in transit. Some butter may crystallize if they solidify too slowly. This does not impact the quality of the butter.</p>
    </div>

    <p class="credits credits--distributor">Distributed By Halden Trade LLC<br>Brookfield, DE 19900</p>
    <p class="credits credits--producer">Produced in Ghana By:<br>Koforo Ghana Ltd<br>www.koforo-example.com</p>
  </section>

  <p class="spec spec--front">Dimension:W = 7.48 InchesH = 10.43 inche</p>
  <p class="spec spec--back">Dimension:W = 7.48 InchesH = 10.43 inche</p>
</main>
</body>
</html>
```